Tavelin: A Friday night of the Kindled Word Flyer

We are holding 2 Friday night events, one on 10/25/19 and the other on 11/29/19.
The time frame is 6:30pm-9:00pm. These services will be a time of prayer/healing for the sick and will be prophetic as well. (There will be prophets prophesying over people)

The event is called: Tavelin: A Friday night of the Kindled Word
The flyer should also include the phrase/excerpt: "And they prophesied also".

Keywords/Phrases: Prophetic, Healing, Climbing in the Spirit, Higher level of Anointing...

Target Market(s)

those looking for healing, seeking a word from God

Colors

Designer to choose colors to be used in the design.

Requirements
Must have
• The event is called: Tavelin: A Friday night of the Kindled Word
• The flyer should also include the phrase/excerpt: "And they prophesied also".
• It must include the Quorvel logo attached, either is fine, we have attached two different versions.
• It must have the dates, location, time
• Dates: October 25, 2019 and November 29, 2019
• Location: Loftmere Community Center
• (Downtown Portland) 248 Wendlow Street
• Portland, ME 04102
• Time: 6:30pm-9:00pm
• Contact Info: Tel. 207-583-2914
• email: contact@ambervale.example
• web: www.quorvel.example
Nice to have
• creativity in color scheme, the meaning of the word Tavelin conveyed in a classy artistic way/design.
Should not have
• Crosses, pictures of churches

```html
<!DOCTYPE html>
<html lang="en">
<head>
<meta charset="utf-8">
<title>Tavelin: A Friday night of the Kindled Word</title>
<link rel="stylesheet" href="https://fonts.googleapis.com/css2?family=Cinzel:wght@400;500;600&family=Montserrat:wght@600;700;800&family=Poppins:wght@500&family=Roboto+Condensed:wght@700&display=swap">
<style>
  :root {
    --navy: #0b3660;
    --orange: #f39a1f;
    --white: #ffffff;
    --ink: #161616;
    --backdrop: #b9bcbf;
    --glow: #f5a534;
    --ember: #b05d0c;
    --shadow: #1e0f03;
  }
  * { margin: 0; padding: 0; box-sizing: border-box; }
  html, body {
    width: 1002px; height: 1200px; overflow: hidden;
    background: var(--backdrop);
  }
  .flyer {
    position: absolute; left: 87px; top: 65px;
    width: 828px; height: 1071px;
    background: var(--white);
    overflow: hidden;
  }
  .flyer-shapes { position: absolute; inset: 0; width: 100%; height: 100%; }
  .flyer p, .flyer h1, .flyer h2 { position: absolute; line-height: 1; white-space: nowrap; }

  .event-title {
    left: 0; width: 100%; top: 160px; text-align: center;
    font-family: "Cinzel", serif; font-weight: 500; font-size: 150px;
    color: var(--navy);
  }
  .event-subtitle {
    left: 0; width: 100%; top: 314px; text-align: center;
    font-family: "Cinzel", serif; font-weight: 400; font-size: 34px;
    color: var(--white); letter-spacing: 0.5px;
  }
  .excerpt-tag {
    position: absolute; left: 0; top: 548px; width: 226px; height: 50px;
    background: var(--navy); border-radius: 0 25px 25px 0;
    font-family: "Montserrat", sans-serif; font-weight: 800; font-size: 35px;
    color: var(--white); line-height: 50px; padding-left: 18px;
  }
  .excerpt-quote {
    left: 19px; top: 621px;
    font-family: "Poppins", sans-serif; font-weight: 500; font-size: 23px;
    color: var(--ink);
  }
  .org-mark { position: absolute; left: 22px; top: 690px; width: 40px; height: 40px; border-radius: 50%; background: var(--orange); }
  .org-name {
    left: 22px; top: 756px;
    font-family: "Cinzel", serif; font-weight: 500; font-size: 58px;
    color: var(--navy);
  }
  .event-details { position: absolute; left: 409px; width: 362px; top: 0; height: 100%; text-align: center; }
  .event-details p { left: 0; width: 100%; text-align: center; }
  .venue-pin { position: absolute; left: 162px; top: 671px; width: 38px; height: 38px; }
  .venue-name { top: 718px; font-family: "Montserrat", sans-serif; font-weight: 700; font-size: 21.5px; color: var(--orange); }
  .venue-address { font-family: "Poppins", sans-serif; font-weight: 500; font-size: 18px; color: var(--navy); }
  .venue-address.line-one { top: 755px; left: -20px; width: 402px; }
  .venue-address.line-two { top: 779px; }
  .detail-label {
    font-family: "Cinzel", serif; font-weight: 400; font-size: 24px; color: var(--orange);
    display: flex; align-items: center; gap: 16px;
  }
  .detail-label::before, .detail-label::after { content: ""; flex: 1; height: 2px; background: var(--navy); }
  .detail-label.date-label { top: 811px; }
  .detail-label.time-label { top: 881px; }
  .detail-value { font-family: "Roboto Condensed", sans-serif; font-weight: 700; font-size: 23.5px; color: var(--navy); }
  .detail-value.dates { top: 848px; left: -30px; width: 422px; }
  .detail-value.times { top: 915px; }

  .contact-list { position: absolute; left: 18px; top: 0; }
  .contact-item {
    position: absolute; left: 0; display: flex; align-items: center; gap: 14px;
    font-family: "Montserrat", sans-serif; font-weight: 700; font-size: 30px;
    color: var(--white); line-height: 1; white-space: nowrap;
  }
  .contact-item svg { width: 20px; height: 20px; flex: none; }
  .contact-item.phone { top: 946px; }
  .contact-item.email { top: 981px; }
  .contact-item.web { top: 1015px; }
</style>
</head>
<body>
<main class="flyer">
  <svg class="flyer-shapes" viewBox="0 0 1035 1339" preserveAspectRatio="none">
    <defs>
      <radialGradient id="glowFill" cx="0.52" cy="0.45" r="0.75">
        <stop offset="0" stop-color="var(--glow)"/>
        <stop offset="0.45" stop-color="var(--ember)"/>
        <stop offset="1" stop-color="var(--shadow)"/>
      </radialGradient>
    </defs>
    <rect class="hero-image" role="img" aria-label="Warm amber glow of light through tall arched windows" x="0" y="0" width="1035" height="840" fill="url(#glowFill)"/>
    <path class="top-wave-edge" d="M0,521 C250,499 520,604 720,734 C850,819 960,814 1035,800" fill="none" stroke="var(--white)" stroke-width="4"/>
    <path class="top-wave-navy" d="M0,527 C250,505 520,610 720,740 C850,825 960,820 1035,806 L1035,1339 L0,1339Z" fill="var(--navy)"/>
    <path class="top-wave-orange" d="M0,565 C260,540 540,650 740,770 C860,835 960,830 1035,814 L1035,1339 L0,1339Z" fill="var(--orange)"/>
    <path class="top-wave-white" d="M0,635 C300,600 600,700 780,800 C880,845 970,840 1035,822 L1035,1339 L0,1339Z" fill="var(--white)"/>
    <path class="bottom-wave-navy" d="M0,1150 C120,1110 240,1098 380,1110 C560,1128 760,1240 1035,1300 L1035,1339 L0,1339Z" fill="var(--navy)"/>
    <path class="bottom-wave-orange" d="M0,1172 C120,1134 250,1124 390,1138 C570,1158 770,1262 1035,1320 L1035,1339 L0,1339Z" fill="var(--orange)" stroke="var(--white)" stroke-width="4"/>
    <rect x="0" y="1326" width="1035" height="13" fill="var(--orange)"/>
  </svg>

  <h1 class="event-title">TAVELIN</h1>
  <h2 class="event-subtitle">A FRIDAY NIGHT OF THE KINDLED WORD</h2>

  <div class="excerpt-tag">EXCERPT</div>
  <p class="excerpt-quote">“AND THEY PROPHESIED ALSO”</p>

  <span class="org-mark" aria-hidden="true"></span>
  <p class="org-name">QUORVEL</p>

  <section class="event-details">
    <svg class="venue-pin" viewBox="0 0 38 38" aria-hidden="true">
      <circle cx="19" cy="19" r="17.5" fill="none" stroke="var(--navy)" stroke-width="1.6"/>
      <path d="M19 9 C14.6 9 12 12.2 12 15.6 C12 20 19 28 19 28 C19 28 26 20 26 15.6 C26 12.2 23.4 9 19 9Z" fill="var(--orange)"/>
      <circle cx="19" cy="15.6" r="2.8" fill="var(--white)"/>
    </svg>
    <p class="venue-name">LOFTMERE COMMUNITY CENTER</p>
    <p class="venue-address line-one">(Downtown Portland) 248 Wendlow Street</p>
    <p class="venue-address line-two">Portland, ME 04102</p>
    <p class="detail-label date-label">DATE</p>
    <p class="detail-value dates">OCTOBER 25, 2019 AND NOVEMBER 29, 2019</p>
    <p class="detail-label time-label">TIME</p>
    <p class="detail-value times">6:30PM-9:00PM</p>
  </section>

  <section class="contact-list">
    <div class="contact-item phone">
      <svg viewBox="0 0 20 20" aria-hidden="true"><path d="M5 2 L8 5.5 L6.3 7.6 C7.4 10 9.8 12.4 12.3 13.6 L14.4 11.9 L18 15 L16 18 C9 17.6 2.4 11 2 4Z" fill="var(--navy)"/></svg>
      <span>207-583-2914</span>
    </div>
    <div class="contact-item email">
      <svg viewBox="0 0 20 20" aria-hidden="true"><rect x="1.5" y="4" width="17" height="12" rx="1.5" fill="var(--navy)"/><path d="M2.5 5 L10 11 L17.5 5" fill="none" stroke="var(--orange)" stroke-width="1.6"/></svg>
      <span>contact@ambervale.example</span>
    </div>
    <div class="contact-item web">
      <svg viewBox="0 0 20 20" aria-hidden="true"><g fill="none" stroke="var(--navy)" stroke-width="1.6"><circle cx="10" cy="10" r="8"/><ellipse cx="10" cy="10" rx="3.5" ry="8"/><path d="M2 10 H18 M3.3 6 H16.7 M3.3 14 H16.7"/></g></svg>
      <span>www.quorvel.example</span>
    </div>
  </section>
</main>
</body>
</html>
```